Guardwell Field Partners

KRU K.V.R.E./ENVIRONMENTAL MANAGEMENT. Member of T.R.P.K., N.V.L.T.. R.K.W.P., G.F.N.Y. K.V.R.E. 10/20/30 hr. GENERAL INDUSTRY CERTIFIED, HAZMAT CERTIFIED, CONSTRUCTION SAFETY CERTIFIED, K.V.R.E. LOG, LOSS PREVENTION SOLUTIONS, WILL WRITE SAFETY PROTOCOL PROGRAMS ACCORDING TO LOCAL AND STATE CODES/STANDARDS. INSPECT YOUR PLACE OF BUSINESS INSIDE AND OUT SIDE INFRASTRUCTURE INCLUDING SAFETY INSPECTION PROTOCOL REGARDING EQUIPMENT, PUMP HOUSE, COMPRESSOR LOG AND FIRE RISERS MANDATES. CONDUCT FIRE EVACUATIONS AND CREATE EVACUATION MASS AS REQUIRED BY LAW. TRAINING YOU AND YOUR SUPERVISORS TO CREATE A SAFETY CULTURE. INVESTIGATE ACCIDENTS AND DOCUMENT FOLLOW UP. WALK WITH CITY AND STATE CODES COMPLIANCE OFFICERS AS A CONDUCT AND AND FOLLOW THROUGH WITH REQUIRED CHANCES IN CODE COMPLIANCE. 15 YEARS EXPERIENCE.

Target Market(s)

businesses with 11+ employees as mandated by Federal law. Business owners.

Industry/Entity Type

Business

Contact Information for Business Card

MARLA K. FENWICK
418 N.E. HOLLOWMERE LANE
PORT SAINT LUCIE , FLORIDA
34871-2046

www.guardwellfieldpartners.us
Rkt418@plovmail.net
(877) 315-6042

Requirements
Must have
• Safety training, inspections, images, knowledge, teamwork, safety culture, safe workplace, compliance, 15 years experience, training documenting all trying development, trying needs analysis, proactive and reactive observations, technical writing programs, creating power point materials for training modules, excel spreadsheet.

```html
<!DOCTYPE html>
<html lang="en">
<head>
<meta charset="utf-8">
<title>Guardwell Field Partners – Business Card</title>
<link rel="stylesheet" href="https://fonts.googleapis.com/css2?family=Fira+Sans+Condensed:wght@600;700&family=Open+Sans:wght@400;500;600&display=swap">
<style>
  :root {
    --page-bg: #ecebe8;
    --navy: #1f3f86;
    --navy-light: #3f66b8;
    --red: #e3262b;
    --deep-red: #8a1f1c;
    --ink-dark: #2a2a2a;
    --white: #ffffff;
    --photo-light: #b9c9c4;
    --photo-dark: #5f7a3a;
  }
  html, body {
    margin: 0;
    width: 1200px;
    height: 1200px;
    overflow: hidden;
    background: var(--page-bg);
  }
  .business-card {
    position: absolute;
    left: 50px;
    top: 278px;
    width: 1100px;
    height: 644px;
    box-shadow: 0 6px 20px rgba(0,0,0,0.25);
  }
  .owner-name {
    font-family: "Fira Sans Condensed", sans-serif;
    font-weight: 700;
    font-size: 27px;
    fill: var(--white);
  }
  .contact-line {
    font-family: "Open Sans", sans-serif;
    font-weight: 500;
    font-size: 20px;
    fill: var(--white);
  }
  .years-number {
    font-family: "Fira Sans Condensed", sans-serif;
    font-weight: 600;
    font-size: 76px;
    fill: var(--red);
  }
  .years-label {
    font-family: "Fira Sans Condensed", sans-serif;
    font-weight: 700;
    font-size: 39px;
    fill: var(--deep-red);
  }
  .experience-label {
    font-family: "Fira Sans Condensed", sans-serif;
    font-weight: 700;
    font-size: 19px;
    fill: var(--ink-dark);
  }
  .service-line {
    font-family: "Open Sans", sans-serif;
    font-size: 23.5px;
    fill: var(--white);
    text-shadow: 0 1px 3px rgba(0,0,0,0.85);
  }
  .website {
    font-family: "Open Sans", sans-serif;
    font-weight: 600;
    font-size: 20px;
    fill: var(--white);
  }
</style>
</head>
<body>
<svg class="business-card" viewBox="0 0 820 480" xmlns="http://www.w3.org/2000/svg">
  <defs>
    <linearGradient id="photoTones" x1="0" y1="0" x2="0" y2="1">
      <stop offset="0" stop-color="var(--photo-light)"/>
      <stop offset="1" stop-color="var(--photo-dark)"/>
    </linearGradient>
    <linearGradient id="redFade" x1="0" y1="0" x2="1" y2="0">
      <stop offset="0" stop-color="var(--red)"/>
      <stop offset="0.42" stop-color="var(--red)"/>
      <stop offset="0.62" stop-color="var(--red)" stop-opacity="0.35"/>
      <stop offset="0.75" stop-color="var(--red)" stop-opacity="0"/>
    </linearGradient>
  </defs>

  <rect class="photo-area" x="0" y="0" width="820" height="428" fill="url(#photoTones)"
        role="img" aria-label="Photo placeholder: businessman standing in a green wheat field under an open sky"/>

  <rect class="services-band" x="0" y="218" width="820" height="210" fill="url(#redFade)"/>

  <polygon class="header-accent" points="0,0 672,0 492,224 0,218" fill="var(--navy-light)"/>
  <polygon class="header-panel" points="0,0 650,0 478,214 0,210" fill="var(--navy)"/>

  <polygon class="footer-accent" points="0,428 820,420 820,432 0,434" fill="var(--navy-light)"/>
  <rect class="footer-band" x="0" y="432" width="820" height="48" fill="var(--navy)"/>

  <text class="owner-name" x="40" y="62">MARLA K</text>
  <text class="contact-line" x="40" y="95">Fenwick 418 N.E Hollowmere lane port saint lucie</text>
  <text class="contact-line" x="40" y="124">florida 34871-2046</text>

  <g class="icon-mail" transform="translate(42,151)">
    <rect x="0" y="0" width="19" height="13" fill="var(--white)"/>
    <polyline points="0,0 9.5,7.5 19,0" fill="none" stroke="var(--navy)" stroke-width="1.5"/>
  </g>
  <text class="contact-line" x="73" y="162">Rkt418@plovmail.net</text>

  <g class="icon-phone" transform="translate(41,178)" fill="var(--white)">
    <path d="M2 6 Q10 0 18 6 L16 9 Q10 6 4 9 Z"/>
    <rect x="5" y="9" width="10" height="9" rx="1.5"/>
    <rect x="8" y="11.5" width="4" height="4" fill="var(--navy)"/>
  </g>
  <text class="contact-line" x="73" y="195">(877) 315-6042</text>

  <text class="years-number" x="731" y="95" text-anchor="middle">15</text>
  <text class="years-label" x="731" y="130" text-anchor="middle" textLength="113" lengthAdjust="spacingAndGlyphs">YEARS</text>
  <text class="experience-label" x="731" y="150" text-anchor="middle" textLength="112" lengthAdjust="spacingAndGlyphs">EXPERIENCE</text>

  <g class="services" text-anchor="middle">
    <text class="service-line" x="410" y="255">Safety training, inspections, images, knowledge, teamwork</text>
    <text class="service-line" x="410" y="285">safety culture, safe workplace, compliance</text>
    <text class="service-line" x="410" y="316">training documenting all trying development, trying needs analysis</text>
    <text class="service-line" x="410" y="348">proactive and reactive observations, technical writing programs</text>
    <text class="service-line" x="410" y="379">creating power point materials for training modules</text>
    <text class="service-line" x="408" y="410">excel spreadsheet.</text>
  </g>

  <text class="website" x="410" y="461" text-anchor="middle">WWW.GUARDWELLFIELDPARTNERS.US</text>
</svg>
</body>
</html>
```